Allstar cheerleading team sign ups

We need a flyer to send out to the local schools as well as to put on our website and facebook page.

We are an allstar cheerleading gym that offers competitive cheerleading teams.

We are rolling out a new program called "Half Year Teams". The design is geared towards parents, but should also catch the eye of kids.

Industry/Entity Type

Gym

Requirements
Must have
• Do you want to be an allstar cheerleader? Brindlewood Summit Cheerleading has been one of the top cheerleading training facilities since 2004! Now is your chance to join our family of cheer with less commitment and a fraction of the cost! We are excited to introduce "Half Year Teams"!

The season will run from December to April with each team competing at 3 local competitions. This is a great way to try allstar cheerleading or to cheer during the school offseason!

Team Placement*: Saturday, December 1st at 10:30am
(*Everyone makes a team)

Cost: $115 per month (includes 1 practice per week, choreography/music fees, competition fees)

Uniform: $175 (includes skirt, top, briefs, bow, shoes)

Practice Times: Thursdays 6:45pm-8:30pm

All ages welcome!

www.brindlewood-summit.example
704-219-8853
48216-K Ferncastle Avenue, Charlotte, NC 28941

Must have pictures!

Our colors are carolina blue, black and white- should follow that color scheme.

I am attaching our "Free Classes" flyer to show you an example of what type of design we like.

The logo I am sending is the wrong blue. It should be a light or carolina blue.

```html
<!DOCTYPE html>
<html lang="en">
<head>
<meta charset="utf-8">
<title>Half Teams – Brindlewood Summit Cheerleading</title>
<link rel="stylesheet" href="https://fonts.googleapis.com/css2?family=Archivo+Black&family=Arimo:wght@700&display=swap">
<style>
  :root {
    --carolina: #86c1e8;
    --carolina-deep: #5e8fb3;
    --ink: #0b0f14;
    --paper: #ffffff;
    --photo-dark: #2b3a48;
    --photo-mid: #6f8799;
    --photo-light: #b9c6cf;
  }
  * { margin: 0; padding: 0; box-sizing: border-box; }
  html, body { width: 900px; height: 1200px; overflow: hidden; background: var(--paper); }
  .flyer { position: relative; width: 900px; height: 1200px; background: var(--paper); font-family: "Arimo", Arial, sans-serif; }

  .hero-photo {
    position: absolute; left: 0; top: 0; width: 900px; height: 292px;
    background: linear-gradient(100deg, var(--photo-dark) 0%, var(--photo-mid) 35%, var(--photo-dark) 55%, var(--photo-mid) 80%, var(--photo-dark) 100%);
  }
  .headline { position: absolute; left: 0; top: 0; width: 900px; height: 292px; }
  .headline span { position: absolute; font-family: "Archivo Black", "Arial Black", sans-serif; line-height: 1; white-space: nowrap; }
  .headline .lead { left: 78px; top: 62px; font-size: 38px; color: var(--paper);
    text-shadow: -2px -2px 0 var(--ink), 2px -2px 0 var(--ink), -2px 2px 0 var(--ink), 2px 2px 0 var(--ink), 4px 4px 4px rgba(0,0,0,.6); }
  .headline .big { color: var(--carolina);
    text-shadow: -3px -3px 0 var(--ink), 3px -3px 0 var(--ink), -3px 3px 0 var(--ink), 3px 3px 0 var(--ink), 0 3px 0 var(--ink), 3px 0 0 var(--ink), 6px 6px 6px rgba(0,0,0,.6); }
  .headline .line-one { left: 135px; top: 140px; font-size: 70px; }
  .headline .line-two { left: 222px; top: 212px; font-size: 72px; }

  .action-photo {
    position: absolute; left: 0; top: 308px; width: 373px; height: 563px;
    background: radial-gradient(ellipse at 45% 45%, var(--photo-light) 0%, var(--photo-mid) 45%, var(--photo-dark) 100%);
  }

  .brand { position: absolute; left: 0; top: 871px; width: 387px; height: 329px; text-align: center; }
  .brand-name { position: absolute; left: 20px; top: 36px; width: 347px; font-family: "Archivo Black", "Arial Black", sans-serif;
    font-size: 36px; line-height: 1.2; color: var(--carolina-deep); text-transform: uppercase; }
  .contact { position: absolute; left: 0; top: 226px; width: 387px; font-size: 16.5px; line-height: 1.28; color: var(--ink); }

  .details { position: absolute; left: 387px; top: 308px; width: 513px; height: 892px; background: var(--carolina);
    color: var(--paper); text-align: center; text-shadow: 2px 2px 3px rgba(0,0,0,.55); }
  .details > * { position: absolute; left: 0; width: 513px; }
  .details .title { top: 20px; font-family: "Archivo Black", "Arial Black", sans-serif; font-size: 45px; letter-spacing: 1px; }
  .details .pitch { top: 78px; font-size: 22.5px; line-height: 1.27; padding: 0 30px; }
  .details .intro { top: 196px; font-size: 14px; }
  .details .program { top: 226px; font-family: "Archivo Black", "Arial Black", sans-serif; font-size: 33px; }
  .details .program-rule { top: 268px; left: 99px; width: 297px; height: 4px; background: var(--paper); box-shadow: 2px 2px 3px rgba(0,0,0,.55); }
  .details .info { font-size: 20.5px; line-height: 1.3; }
  .details .placement { top: 310px; }
  .details .cost { top: 446px; }
  .details .uniform { top: 608px; }
  .details .practice { top: 738px; }
  .details .welcome { top: 768px; font-size: 27px; }
  .details .welcome { top: 794px; }
  .details .practice { top: 714px; }
  .details .tagline { top: 822px; font-size: 18px; line-height: 1.2; }
</style>
</head>
<body>
<main class="flyer">
  <div class="hero-photo" role="img" aria-label="Photo of cheerleaders in team uniforms seen from behind"></div>
  <h1 class="headline">
    <span class="lead">WANT TO BE AN</span>
    <span class="big line-one">ALL-STAR</span>
    <span class="big line-two">CHEERLEADER?</span>
  </h1>

  <div class="action-photo" role="img" aria-label="Photo of a cheerleader performing a jump with teammates behind"></div>

  <section class="brand">
    <p class="brand-name">Brindlewood Summit Cheerleading</p>
    <p class="contact">www.brindlewood-summit.example<br>704-219-8853<br>48216-K Ferncastle Avenue,<br>Charlotte, NC 28941</p>
  </section>

  <section class="details">
    <h2 class="title">JOIN THE FAMILY</h2>
    <p class="pitch">Now is your chance to join with less commitment and a fraction of the cost!</p>
    <p class="intro">INTRODUCING</p>
    <h3 class="program">HALF TEAMS</h3>
    <div class="program-rule"></div>
    <p class="info placement">Team Placement:<br>Saturday, December 1st at 10:30 am<br>(Everyone makes a team)</p>
    <p class="info cost">Cost: $115 per month<br>(includes 1 practice per week,<br>choreography/music fees,<br>competition fees)</p>
    <p class="info uniform">Uniform: $175<br>(includes skirt, top, briefs,<br>bow, shoes)</p>
    <p class="info practice">Practice Times:<br>Thursdays 6:45 pm - 8:30 pm</p>
    <p class="welcome">All ages welcome!</p>
    <p class="tagline">one of the top cheerleading<br>training facilities since 2004</p>
  </section>
</main>
</body>
</html>
```